brisk-vale.com Real Estate, Investment, Financial corporate

Real Estate, Investment, Financial corporate looking site. Show present a professional firm, with an elegant display. Please see the attached file which includes the logo, palette and fonts.
Updates

We just starting the brief today. ( logo was delayed)

Target Market(s)

Investors, Corporate , B2b

Industry/Entity Type

real-estate investments

Number of Pages Required

3 page

Requirements
Must have
• Dazzling Homepage
Nice to have
• paralex

```html
<!DOCTYPE html>
<html lang="en">
<head>
<meta charset="utf-8">
<title>Briskvale — Real Estate, Investment, Financial Corporate</title>
<link rel="stylesheet" href="https://fonts.googleapis.com/css2?family=Nunito+Sans:ital,wght@0,400;0,600;0,700;0,800;0,900;1,400&display=swap">
<style>
:root{
  --orange:#ff8a3d;
  --orange-deep:#ff6f12;
  --ink:#222;
  --body:#666;
  --dark:#111213;
  --white:#fff;
}
*{margin:0;padding:0;box-sizing:border-box}
html,body{width:1200px;height:3345px;overflow:hidden}
body{font-family:"Nunito Sans",Arial,sans-serif;color:var(--ink);background:var(--white);position:relative}
.abs{position:absolute}
.btn{position:absolute;background:var(--orange);color:#fff;font-weight:800;font-size:15px;display:flex;align-items:center;justify-content:center;letter-spacing:.3px}
.lorem{font-size:11.5px;line-height:21px;color:var(--body)}
.photo{position:absolute;box-shadow:0 6px 18px rgba(0,0,0,.18)}

/* hero */
.hero{position:absolute;left:0;top:0;width:1200px;height:713px;
  background:
    radial-gradient(ellipse 170px 300px at 300px 420px,rgba(245,232,220,.55),transparent 70%),
    radial-gradient(ellipse 120px 90px at 345px 250px,rgba(214,170,140,.55),transparent 75%),
    radial-gradient(ellipse 230px 330px at 880px 420px,rgba(120,110,140,.55),transparent 70%),
    radial-gradient(ellipse 130px 120px at 840px 230px,rgba(200,165,120,.5),transparent 75%),
    radial-gradient(ellipse 260px 160px at 120px 640px,rgba(150,110,70,.5),transparent 75%),
    linear-gradient(110deg,#2f2a27 0%,#58493f 35%,#4a4352 65%,#27252c 100%)}
.hero-shade{position:absolute;inset:0;background:linear-gradient(180deg,rgba(0,0,0,.55) 0%,rgba(0,0,0,.1) 22%,rgba(0,0,0,.15) 80%,rgba(0,0,0,.3) 100%)}
.hero-block{position:absolute;left:408px;top:132px;width:372px;height:454px;background:rgba(255,120,40,.32)}
.logo{position:absolute;left:60px;top:18px;font-size:32px;font-weight:900;color:#fff;letter-spacing:-.5px}
.nav{position:absolute;left:555px;top:36px;display:flex;gap:21px;font-size:11px;color:#fff;letter-spacing:.2px}
.nav .on{color:var(--orange);border-bottom:1px solid var(--orange);padding-bottom:6px}
.nav-social{position:absolute;left:980px;top:34px;display:flex;gap:13px}
.nav-social span{width:17px;height:17px;border-radius:50%;border:1.5px solid rgba(255,255,255,.9)}
.nav-social span:first-child{border-color:var(--orange)}
.call{position:absolute;left:1106px;top:26px;width:34px;height:34px;border-radius:50%;background:var(--orange);display:flex;align-items:center;justify-content:center}
.kicker{position:absolute;left:0;width:1200px;top:292px;text-align:center;color:#fff;font-size:15px;letter-spacing:6px;font-weight:600}
.hero-title{position:absolute;left:0;width:1200px;top:312px;text-align:center;color:#fff;font-size:78px;line-height:96px;font-weight:800;letter-spacing:-1px}
.hero-sub{position:absolute;left:0;width:1200px;top:410px;text-align:center;color:#fff;font-size:16px}

/* services */
.services{position:absolute;left:0;top:713px;width:1200px;height:604px;background:var(--orange)}
.sec-title{position:absolute;left:0;width:1200px;text-align:center;font-size:34px;font-weight:900}
.sec-sub{position:absolute;left:0;width:1200px;text-align:center;font-size:13.5px;font-style:italic}
.svc .frame{position:absolute;border:1px solid rgba(255,255,255,.8)}
.svc .back{position:absolute;background:var(--orange-deep)}
.svc h3{position:absolute;color:#fff;font-size:19px;font-weight:800}
.svc p{position:absolute;color:#fff;font-size:11px;line-height:19.5px;width:275px}

/* welcome */
.welcome-photo{position:absolute;left:590px;top:1317px;width:610px;height:430px;
  background:
    radial-gradient(ellipse 90px 150px at 345px 170px,rgba(40,48,66,.95),transparent 80%),
    radial-gradient(ellipse 60px 140px at 150px 200px,rgba(200,204,210,.9),transparent 80%),
    radial-gradient(ellipse 220px 120px at 420px 400px,rgba(190,196,204,.7),transparent 80%),
    linear-gradient(100deg,#f4f5f7 0%,#c8ccd2 16%,#2f3542 45%,#262b36 70%,#5f646e 100%)}

/* portfolio */
.portfolio{position:absolute;left:0;top:1747px;width:1200px;height:488px;background:linear-gradient(180deg,#e3e4e6,#cdd0d4 60%,#eceded)}
.pf-block{position:absolute;left:787px;top:1747px;width:413px;height:488px;background:var(--orange)}
.pf-inner{position:absolute;left:866px;top:1838px;width:250px;height:298px;background:linear-gradient(180deg,#f2f3f5,#d5d8dc 60%,#bfc3c8)}

/* news */
.news-card h4{position:absolute;width:280px;font-size:13px;line-height:21px;font-weight:800;color:#333}
.news-card p{position:absolute;width:280px;font-size:10.5px;line-height:19.5px;color:var(--body)}
.news-card .date{position:absolute;width:40px;height:50px;background:var(--orange);color:#fff;text-align:center;font-weight:800;font-size:22px;line-height:24px;padding-top:4px}
.news-card .date small{display:block;font-size:10px;line-height:12px;font-weight:700}
.news-card .more{position:absolute;font-size:12px;font-weight:700;color:var(--orange);text-decoration:underline}
.news-card .rule{position:absolute;height:1px;background:#ddd}
.news-card .photo{width:278px;height:205px;box-shadow:none}

/* cta + footer */
.footer{position:absolute;left:0;top:2935px;width:1200px;height:410px;background:var(--dark)}
.cta{position:absolute;left:139px;top:2850px;width:922px;height:192px;background:var(--orange)}
.cta h2{position:absolute;left:70px;top:52px;color:#fff;font-size:24px;line-height:34px;font-weight:800}
.cta p{position:absolute;left:70px;top:123px;color:#fff;font-size:14px;font-style:italic;opacity:.9}
.cta .outline{position:absolute;border:1px solid #fff;color:#fff;font-weight:800;font-size:15px;display:flex;align-items:center;justify-content:center;gap:10px}
.f-title{position:absolute;font-size:16.5px;font-weight:800;color:#fff}
.f-title em{font-style:normal;color:var(--orange)}
.f-list{position:absolute;list-style:none;font-size:11.5px;color:#ddd;line-height:22.5px}
.f-list li::before{content:"";display:inline-block;width:5px;height:5px;border-radius:50%;background:var(--orange);margin-right:17px;vertical-align:middle}
.f-text{position:absolute;color:#ddd;font-size:12px;line-height:19px}
.f-social{position:absolute;left:983px;top:3210px;display:flex;gap:7px}
.f-social span{width:34px;height:34px;border-radius:50%;border:1.5px solid #fff;display:flex;align-items:center;justify-content:center}
.f-social span::after{content:"";width:12px;height:12px;border-radius:50%;background:#fff}
.f-social span:first-child{border-color:var(--orange)}
.f-social span:first-child::after{background:var(--orange)}
</style>
</head>
<body>

<!-- Hero -->
<section class="hero" role="img" aria-label="Photo of an estate agent beside a couple viewing a new home">
  <div class="hero-shade"></div>
  <div class="hero-block"></div>
</section>
<div class="logo">Briskvale</div>
<nav class="nav">
  <span class="on">HOME</span><span>ABOUT US</span><span>SERVICES</span><span>PORTFOLIO</span><span>NEWS</span><span>CONTACT US</span>
</nav>
<div class="nav-social" aria-label="Social links"><span></span><span></span><span></span><span></span></div>
<div class="call"><svg width="16" height="16" viewBox="0 0 24 24"><path fill="#fff" d="M6.6 10.8a15 15 0 0 0 6.6 6.6l2.2-2.2a1 1 0 0 1 1-.25 11.4 11.4 0 0 0 3.6.57 1 1 0 0 1 1 1V20a1 1 0 0 1-1 1A17 17 0 0 1 3 4a1 1 0 0 1 1-1h3.5a1 1 0 0 1 1 1c0 1.25.2 2.45.57 3.57a1 1 0 0 1-.25 1z"/></svg></div>
<div class="kicker">REAL ESTATE IS</div>
<h1 class="hero-title">OUR PASSION</h1>
<div class="hero-sub">Real Estate &nbsp;|&nbsp; Investment &nbsp;|&nbsp; Financial Corporate</div>
<div class="btn" style="left:529px;top:466px;width:143px;height:40px">GET ESTIMATE</div>

<!-- Services -->
<section class="services"></section>
<h2 class="sec-title" style="top:782px;color:#fff">SERVICES WE PROVIDE</h2>
<p class="sec-sub" style="top:833px;color:#fff">Lorem Ipsum is simply dummy text of the printing and typesetting industry.</p>

<div class="svc">
  <div class="frame" style="left:131px;top:889px;width:263px;height:162px"></div>
  <div class="back" style="left:152px;top:910px;width:272px;height:182px"></div>
  <div class="photo" role="img" aria-label="Small wooden house model on a desk beside a handshake" style="left:142px;top:900px;width:270px;height:180px;background:radial-gradient(ellipse 50px 60px at 190px 110px,#b88a5c,transparent 80%),radial-gradient(ellipse 90px 50px at 80px 40px,#3a2e28,transparent 80%),linear-gradient(120deg,#2c2622,#8a7a6c 50%,#e6dccf)"></div>
  <h3 style="left:141px;top:1120px">Real Estate</h3>
  <p style="left:142px;top:1153px">Lorem Ipsum is simply dummy text of the printing and typesetting industry. Lorem Ipsum has been the industry's standard dummy...</p>

  <div class="frame" style="left:454px;top:919px;width:263px;height:162px"></div>
  <div class="back" style="left:476px;top:940px;width:271px;height:182px"></div>
  <div class="photo" role="img" aria-label="Stacks of coins with a rising growth chart" style="left:466px;top:930px;width:269px;height:180px;background:radial-gradient(ellipse 110px 35px at 140px 145px,#c9b89a,transparent 80%),radial-gradient(ellipse 80px 50px at 220px 50px,#8aa3bb,transparent 80%),linear-gradient(110deg,#17222f,#34506b 50%,#9eb0c0)"></div>
  <h3 style="left:464px;top:1151px">Investment</h3>
  <p style="left:465px;top:1184px">Lorem Ipsum is simply dummy text of the printing and typesetting industry. Lorem Ipsum has been the industry's standard dummy...</p>

  <div class="frame" style="left:776px;top:889px;width:263px;height:162px"></div>
  <div class="back" style="left:798px;top:910px;width:271px;height:182px"></div>
  <div class="photo" role="img" aria-label="Hands reviewing financial charts on a tablet" style="left:788px;top:900px;width:269px;height:180px;background:radial-gradient(ellipse 80px 55px at 150px 80px,#a9c6dc,transparent 80%),radial-gradient(ellipse 70px 80px at 240px 140px,#1e232c,transparent 80%),linear-gradient(120deg,#eef0f2,#b7c8d6 50%,#39414e)"></div>
  <h3 style="left:786px;top:1120px">Financial Corporate</h3>
  <p style="left:787px;top:1153px">Lorem Ipsum is simply dummy text of the printing and typesetting industry. Lorem Ipsum has been the industry's standard dummy...</p>
</div>

<!-- Welcome -->
<div class="welcome-photo" role="img" aria-label="Architect pointing a pen at a scale model of an apartment building"></div>
<div class="abs" style="left:104px;top:1394px;font-size:14px;color:#333">Welcome To</div>
<h2 class="abs" style="left:103px;top:1414px;font-size:34px;font-weight:900;color:#333">BRISK <span style="color:var(--orange)">VALE</span></h2>
<p class="abs" style="left:104px;top:1474px;width:380px;font-size:14px;line-height:21px;font-style:italic;color:#333">Lorem Ipsum is simply dummy text of the printing and typesetting industry Lorem Ipsum has been.</p>
<p class="abs lorem" style="left:104px;top:1527px;width:400px">Lorem Ipsum is simply dummy text of the printing and typesetting industry. Lorem Ipsum has been the industry's standard dummy text ever since the 1500s, when an unknown printer took a galley of type and scrambled it to make a type specimen book.</p>
<div class="btn" style="left:104px;top:1628px;width:135px;height:40px">LEARN MORE</div>

<!-- Portfolio -->
<section class="portfolio" role="img" aria-label="Faded city skyline backdrop"></section>
<div class="photo" role="img" aria-label="Row of modern townhouses at dusk" style="left:100px;top:1797px;width:300px;height:183px;background:radial-gradient(ellipse 120px 40px at 140px 105px,#d8c7a8,transparent 80%),linear-gradient(180deg,#4d7190,#8d9aa4 45%,#6b6a64 62%,#35342f)"></div>
<div class="abs" style="left:358px;top:1938px;width:42px;height:42px;background:var(--orange);display:flex;align-items:center;justify-content:center">
  <svg width="18" height="18" viewBox="0 0 24 24" fill="none" stroke="#fff" stroke-width="2"><circle cx="10" cy="10" r="6"/><path d="M14.5 14.5 20 20M10 7v6M7 10h6"/></svg>
</div>
<div class="photo" role="img" aria-label="White modern villa with manicured hedges" style="left:100px;top:1999px;width:300px;height:183px;background:radial-gradient(ellipse 90px 60px at 150px 70px,#f7f7f5,transparent 80%),radial-gradient(ellipse 40px 70px at 60px 100px,#2f5a1f,transparent 80%),linear-gradient(180deg,#dfe8f0,#d2d2cc 45%,#6a9a3c 78%,#4a7a26)"></div>
<div class="photo" role="img" aria-label="Lit family house with front lawn at twilight" style="left:417px;top:1870px;width:299px;height:232px;background:radial-gradient(ellipse 90px 70px at 150px 100px,#e8d6b4,transparent 80%),radial-gradient(ellipse 50px 90px at 30px 110px,#1f3320,transparent 80%),linear-gradient(180deg,#34507a,#7d89a0 35%,#8b8778 58%,#4f8a32 80%,#3a6424)"></div>
<div class="pf-block"></div>
<div class="pf-inner" role="img" aria-label="Tall apartment tower"></div>
<div class="abs" style="left:1003px;top:1945px;font-size:32px;font-weight:900;color:#111;line-height:38px">WORK</div>
<div class="abs" style="left:908px;top:1984px;font-size:32px;font-weight:900;color:#fff;line-height:38px">PORTFOLIO</div>

<!-- News -->
<h2 class="sec-title" style="top:2305px;color:#333">LATEST <span style="color:var(--orange)">NEWS</span></h2>
<p class="sec-sub" style="top:2356px;color:#333">Lorem Ipsum is simply dummy text of the printing and typesetting industry.</p>

<div class="news-card">
  <div class="photo" role="img" aria-label="Two business people looking up at an office building" style="left:146px;top:2412px;background:radial-gradient(ellipse 50px 90px at 200px 120px,#e0ddd6,transparent 80%),radial-gradient(ellipse 70px 110px at 60px 80px,#15161a,transparent 80%),linear-gradient(120deg,#1e1f22,#6f675a 55%,#c9b89a)"></div>
  <div class="date" style="left:150px;top:2540px">10<small>Aug</small></div>
  <h4 style="left:142px;top:2637px">Lorem Ipsum is simply dummy text of the printing and typesetting industry.</h4>
  <p style="left:142px;top:2688px">Lorem Ipsum is simply dummy text of the printing is and typesetting industry. Lorem Ipsum has been the industry's standard dummy text ever since.</p>
  <span class="more" style="left:143px;top:2762px">Read More</span>
  <div class="rule" style="left:210px;top:2775px;width:203px"></div>

  <div class="photo" role="img" aria-label="Hand signing papers beside a house model and coins" style="left:461px;top:2412px;background:radial-gradient(ellipse 80px 50px at 150px 120px,#b8926a,transparent 80%),radial-gradient(ellipse 120px 40px at 140px 185px,#e6e2dc,transparent 80%),linear-gradient(120deg,#16171a,#4d4b48 50%,#d6c9b2)"></div>
  <div class="date" style="left:465px;top:2540px">10<small>Aug</small></div>
  <h4 style="left:459px;top:2637px">Lorem Ipsum is simply dummy text of the printing and typesetting industry.</h4>
  <p style="left:459px;top:2688px">Lorem Ipsum is simply dummy text of the printing is and typesetting industry. Lorem Ipsum has been the industry's standard dummy text ever since.</p>
  <span class="more" style="left:460px;top:2762px">Read More</span>
  <div class="rule" style="left:527px;top:2775px;width:203px"></div>

  <div class="photo" role="img" aria-label="Team meeting around a table with charts" style="left:776px;top:2412px;background:radial-gradient(ellipse 110px 50px at 170px 130px,#dce5ee,transparent 80%),radial-gradient(ellipse 60px 40px at 160px 110px,#3fa0d8,transparent 80%),linear-gradient(120deg,#162540,#3e6291 50%,#c8d2dc)"></div>
  <div class="date" style="left:780px;top:2540px">10<small>Aug</small></div>
  <h4 style="left:774px;top:2637px">Lorem Ipsum is simply dummy text of the printing and typesetting industry.</h4>
  <p style="left:774px;top:2688px">Lorem Ipsum is simply dummy text of the printing is and typesetting industry. Lorem Ipsum has been the industry's standard dummy text ever since.</p>
  <span class="more" style="left:777px;top:2762px">Read More</span>
  <div class="rule" style="left:843px;top:2775px;width:206px"></div>
</div>

<!-- Footer + CTA -->
<footer class="footer"></footer>
<div class="cta">
  <h2>NEED AN HAVE ANY QUESTION or<br>REAL ESTATE SERVICES HELP ?</h2>
  <p>Lorem Ipsum has been the industry's standard dummy Text.</p>
  <div class="outline" style="left:567px;top:75px;width:142px;height:41px">CONTACT US</div>
  <div class="outline" style="left:717px;top:75px;width:158px;height:41px">
    <svg width="18" height="18" viewBox="0 0 24 24"><path fill="#fff" d="M6.6 10.8a15 15 0 0 0 6.6 6.6l2.2-2.2a1 1 0 0 1 1-.25 11.4 11.4 0 0 0 3.6.57 1 1 0 0 1 1 1V20a1 1 0 0 1-1 1A17 17 0 0 1 3 4a1 1 0 0 1 1-1h3.5a1 1 0 0 1 1 1c0 1.25.2 2.45.57 3.57a1 1 0 0 1-.25 1z"/></svg>123 456 7890
  </div>
</div>

<div class="f-title" style="left:61px;top:3085px">Contact <em>Us</em></div>
<svg class="abs" style="left:60px;top:3126px" width="20" height="22" viewBox="0 0 24 24"><path fill="#ff8a3d" d="M12 2a7 7 0 0 0-7 7c0 5 7 13 7 13s7-8 7-13a7 7 0 0 0-7-7zm0 9.5A2.5 2.5 0 1 1 12 6.5a2.5 2.5 0 0 1 0 5z"/></svg>
<div class="f-text" style="left:95px;top:3124px"><span style="color:var(--orange)">Brisk Vale</span><br>101 -lorem ipsum simple<br>text industry print.</div>
<svg class="abs" style="left:60px;top:3198px" width="18" height="18" viewBox="0 0 24 24"><path fill="#ff8a3d" d="M6.6 10.8a15 15 0 0 0 6.6 6.6l2.2-2.2a1 1 0 0 1 1-.25 11.4 11.4 0 0 0 3.6.57 1 1 0 0 1 1 1V20a1 1 0 0 1-1 1A17 17 0 0 1 3 4a1 1 0 0 1 1-1h3.5a1 1 0 0 1 1 1c0 1.25.2 2.45.57 3.57a1 1 0 0 1-.25 1z"/></svg>
<div class="f-text" style="left:95px;top:3196px;font-size:15px">123 456 7890</div>
<svg class="abs" style="left:60px;top:3236px" width="18" height="14" viewBox="0 0 24 18" fill="none" stroke="#ff8a3d" stroke-width="2"><rect x="1" y="1" width="22" height="16"/><path d="M1 1l11 9 11-9"/></svg>
<div class="f-text" style="left:95px;top:3233px">info@brisk-vale.com</div>

<div class="f-title" style="left:299px;top:3085px">Quick <em>Links</em></div>
<ul class="f-list" style="left:299px;top:3122px"><li>Home</li><li>About</li><li>Services</li><li>Portfolio</li><li>News</li><li>Contact Us</li></ul>

<div class="f-title" style="left:499px;top:3085px">Our <em>Services</em></div>
<ul class="f-list" style="left:499px;top:3122px"><li>Real Estate</li><li>Investment</li><li>Financial Corporate</li></ul>

<div class="abs" style="left:940px;top:3078px;width:200px;text-align:right;font-size:32px;font-weight:900;color:#fff">Briskvale</div>
<div class="abs" style="left:900px;top:3124px;width:240px;text-align:right;font-size:12px;color:#fff">SIGN UP FOR NEWSLETTER !</div>
<div class="abs" style="left:727px;top:3157px;width:297px;height:41px;background:#fff;font-size:12px;color:#666;padding:14px 14px">Enter Email</div>
<div class="btn" style="left:1024px;top:3157px;width:116px;height:41px;font-size:14px">SUBSCRIBE</div>
<div class="f-social" aria-label="Social links"><span></span><span></span><span></span><span></span></div>

<div class="abs" style="left:60px;top:3300px;width:1080px;height:1px;background:#2c2d2f"></div>
<div class="abs" style="left:0;top:3320px;width:1200px;text-align:center;font-size:11px;color:#ddd">©<span style="color:var(--orange)">Brisk Vale</span> - 2021 All rights reserved.</div>

</body>
</html>
```